Clara Joy Halden- Lantern Waltz- Autumn/Winter Tour Dates

I need high res A3 Tour poster for print and for social media JPG sharing of tour dates.
Also needed Facebook/Twitter Banner Cover Photos of these dates.
Text Needed Below
Clara Joy Halden
Lantern Waltz
Autumn/Winter Tour Dates
03/09 Ravensby Folk Festival
21/09 Swindon- Calder Theatre
01/10 Hitchin- Brackwell Folk Club
17/10 Bath- The Anvil
20/10 Sheffield- Upper Dale Croquet Club
24/10 Birmingham- Orchard Lamp Cafe
26/10 Glasgow- The Nook and Jar
27/10 Edinburgh - The Marble Parlour
08/11 Capital Reel and Ballad Festival- The Crooked Heron
25/11 Lewes- Tandem Record Shop- Live In Store
02/12 Cambridge- The Quayside
27/01 Lincolnshire- Fenmarsh Theatre
Tickets/Info: www.clarajoyhalden-music.example/gigs
(Quotes/Reviews To Put On)
"Outstanding, rich and expressive."            "Vibrant and Experimental"
**** BdM                                                               **** Tunepaths
"Impressive and Invigorating"                        "Enchanting" Acoustic Wire UK
tBarks

Updates
I cannot read the tour dates on most of the submissions so far. They need to be visible to viewers.
Thank You.
Please also be as creative and inventive as possible- not bland.

Target Market(s)
Music Fans- Folk Acoustic Americana
Industry/Entity Type
Media
Font styles to use
Requirements
Must have
- My photo featured prominently
- Look classy and not tacky or OTT
- Look elegant, wintery and eye catching
- The dates must be very clear to read
- Links to Website:

Nice to have
- Something innovative and not boring in terms of layout design
- Perhaps fading/ misty or wintery

Should not have
- Any colours that do not match

```html
<!DOCTYPE html>
<html lang="en">
<head>
<meta charset="utf-8">
<title>Clara Joy Halden – Lantern Waltz Tour Poster</title>
<link rel="stylesheet" href="https://fonts.googleapis.com/css2?family=Cormorant+SC:wght@600&family=Lato:wght@400;700&display=swap">
<style>
  :root {
    --backdrop: #e9e9eb;
    --night: #101219;
    --forest-grey: #6b6d78;
    --mist: #a9a7b1;
    --hair-blue: #1a2031;
    --skin-pale: #cfc6cc;
    --band-dark: rgba(9, 10, 15, 0.86);
    --band-grey: rgba(186, 190, 198, 0.95);
    --snow: #ffffff;
    --stripe: #e8eaee;
    --ink: #111317;
    --date-text: #e4e6ea;
  }
  * { margin: 0; padding: 0; box-sizing: border-box; }
  html, body { width: 800px; height: 1200px; overflow: hidden; }
  body { background: var(--backdrop); position: relative; }

  .poster {
    position: absolute; left: 0; top: 34px;
    width: 800px; height: 1131px; overflow: hidden;
    background: var(--night);
  }
  .portrait {
    position: absolute; inset: 0;
    background:
      radial-gradient(ellipse 17% 16% at 47% 52%, var(--skin-pale) 0%, rgba(190,182,192,0.75) 45%, transparent 100%),
      radial-gradient(ellipse 12% 10% at 78% 79%, rgba(175,168,178,0.75) 0%, transparent 100%),
      radial-gradient(ellipse 40% 42% at 46% 60%, var(--hair-blue) 0%, rgba(26,32,49,0.85) 55%, transparent 100%),
      radial-gradient(ellipse 38% 30% at 80% 28%, rgba(169,167,177,0.85) 0%, transparent 100%),
      radial-gradient(ellipse 30% 26% at 18% 20%, rgba(150,150,162,0.6) 0%, transparent 100%),
      radial-gradient(ellipse 30% 40% at 90% 65%, rgba(120,116,128,0.7) 0%, transparent 100%),
      linear-gradient(180deg, #3b3e4a 0%, var(--forest-grey) 28%, #4a4c58 55%, #262833 80%, var(--night) 100%);
  }

  .title {
    position: absolute; left: 0; right: 0; top: 58px;
    text-align: center;
    font-family: "Cormorant SC", "Times New Roman", serif;
    font-weight: 600; color: var(--snow);
    font-size: 41px; line-height: 51px; letter-spacing: 2.5px;
    text-shadow: 0 1px 4px rgba(0,0,0,0.55);
  }

  .tour-band {
    position: absolute; left: 0; bottom: 0;
    width: 800px; height: 247px;
  }
  .tour-band svg { position: absolute; inset: 0; }

  .dates {
    position: absolute; left: 38px; top: 21px;
    font-family: "Lato", Arial, sans-serif; color: var(--date-text);
  }
  .dates h2 { font-size: 13.5px; font-weight: 700; color: var(--snow); margin-bottom: 9px; }
  .dates ol { list-style: none; font-size: 10.5px; line-height: 13.8px; }
  .dates .day { display: inline-block; width: 40px; }

  .info {
    position: absolute; right: 10px; top: 47px;
    font-family: "Lato", Arial, sans-serif; color: var(--ink);
    text-align: right;
  }
  .info .tickets { font-size: 12.5px; font-weight: 700; line-height: 18px; }
  .reviews {
    margin-top: 17px; margin-right: 25px;
    font-size: 10.2px; line-height: 13.4px;
  }
  .reviews p + p { margin-top: 14px; }
</style>
</head>
<body>
  <main class="poster">
    <div class="portrait" role="img" aria-label="Portrait photograph of the singer with long dark hair and a wire and pearl crown in a misty winter forest"></div>

    <h1 class="title">Clara Joy Halden<br>Lantern Waltz</h1>

    <section class="tour-band">
      <svg width="800" height="247" viewBox="0 0 800 247" aria-hidden="true">
        <polygon points="0,0 300,0 540,247 0,247" fill="var(--band-dark)"/>
        <polygon points="300,0 800,0 800,247 540,247" fill="var(--band-grey)"/>
        <g stroke="var(--stripe)" stroke-width="5">
          <line x1="300" y1="0" x2="540" y2="247"/>
          <line x1="316" y1="0" x2="556" y2="247"/>
          <line x1="332" y1="0" x2="572" y2="247"/>
        </g>
      </svg>

      <div class="dates">
        <h2>Autumn/Winter Tour Dates</h2>
        <ol>
          <li><span class="day">03/09</span>Ravensby Folk Festival</li>
          <li><span class="day">21/09</span>Swindon- Calder Theatre</li>
          <li><span class="day">01/10</span>Hitchin- Brackwell Folk Club</li>
          <li><span class="day">17/10</span>Bath- The Anvil</li>
          <li><span class="day">20/10</span>Sheffield- Upper Dale Croquet Club</li>
          <li><span class="day">24/10</span>Birmingham- Orchard Lamp Cafe</li>
          <li><span class="day">26/10</span>Glasgow- The Nook and Jar</li>
          <li><span class="day">27/10</span>Edinburgh - The Marble Parlour</li>
          <li><span class="day">08/11</span>Capital Reel and Ballad Festival- The Crooked Heron</li>
          <li><span class="day">25/11</span>Lewes- Tandem Record Shop- Live In Store</li>
          <li><span class="day">02/12</span>Cambridge- The Quayside</li>
          <li><span class="day">27/01</span>Lincolnshire- Fenmarsh Theatre</li>
        </ol>
      </div>

      <div class="info">
        <p class="tickets">Tickets/Info:<br>www.clarajoyhalden-music.example/gigs</p>
        <div class="reviews">
          <p>"Outstanding, rich and expressive."<br>"Vibrant and Experimental"<br>**** BdM **** Tunepaths</p>
          <p>"Impressive and Invigorating"<br>"Enchanting"<br>Acoustic Wire UK<br>tBarks</p>
        </div>
      </div>
    </section>
  </main>
</body>
</html>
```